The Kestrel Personal Training Studio Information Card

The front and back of card to give people that walk in to our gym. There are a few things to say on the card. But it also needs to be designed in an attractive way. You can make some of the information bullett points or with icons or graphics. Please look at our website at https://thekestrelfitness-example.com/ . The card will be 4" x 9"

Target Market(s)

High End Clientele who want to train in a private gym

Industry/Entity Type

Fitness

Font styles to use
Serif
Sans Serif
Other font styles liked:
• the same font Vorlex uses on the zuntab

Colors
F0912C
F2A743
F7CA91
FBE8D2
FDF5EE

Requirements
Must have
• A cool look

```html
<!DOCTYPE html>
<html lang="en">
<head>
<meta charset="utf-8">
<title>The Kestrel Private Training Studio – Information Card</title>
<link href="https://fonts.googleapis.com/css2?family=Barlow:wght@400;500;600;700&family=Barlow+Semi+Condensed:wght@600;700&family=Montserrat:wght@700&display=swap" rel="stylesheet">
<style>
  :root {
    --backdrop: #9b9b9b;
    --paper: #ffffff;
    --red: #e8323a;
    --ink: #1f1f1f;
    --charcoal: #2a2a2a;
    --logo-grey: #58595b;
    --rule: #9a9a9a;
  }
  * { box-sizing: border-box; margin: 0; padding: 0; }
  html, body { width: 753px; height: 1200px; overflow: hidden; }
  body {
    background: var(--backdrop);
    font-family: "Barlow", Arial, sans-serif;
    color: var(--ink);
    position: relative;
  }
  .card {
    position: absolute;
    top: 240px;
    width: 320px;
    height: 720px;
    background: var(--paper);
    display: flex;
    flex-direction: column;
    box-shadow: 0 8px 18px rgba(0,0,0,.25);
  }
  .card--front { left: 34px; }
  .card--back { left: 399px; }

  .brand {
    height: 96px;
    flex: none;
    display: flex;
    flex-direction: column;
    align-items: center;
    justify-content: center;
    gap: 4px;
  }
  .brand__name {
    display: flex;
    align-items: center;
    gap: 8px;
    font-family: "Montserrat", sans-serif;
    font-weight: 700;
    font-size: 29px;
    letter-spacing: -0.5px;
    color: var(--logo-grey);
    line-height: 1;
  }
  .brand__mark { width: 14px; height: 14px; background: var(--red); }
  .brand__tagline {
    font-family: "Barlow", sans-serif;
    font-weight: 700;
    font-size: 10px;
    letter-spacing: 3.6px;
    color: var(--logo-grey);
  }

  .photo { flex: none; }
  .photo--coaches { height: 294px; background: linear-gradient(160deg, #7c8187 0%, #b9bcbf 45%, #3d3f44 100%); }
  .photo--suspension { height: 301px; background: linear-gradient(160deg, #c89467 0%, #a06a40 50%, #3e4456 100%); }

  .headline-band {
    height: 88px;
    flex: none;
    background: var(--red);
    color: #fff;
    font-family: "Barlow Semi Condensed", sans-serif;
    font-weight: 700;
    font-size: 19.5px;
    line-height: 1.25;
    text-align: center;
    display: flex;
    align-items: center;
    justify-content: center;
  }

  .body-copy {
    flex: 1;
    background: linear-gradient(90deg, #ededed 0%, #fbfbfb 30%, #fbfbfb 70%, #e4e4e4 100%);
    text-align: center;
    font-size: 10.6px;
    line-height: 1.32;
    padding: 14px 22px 0;
  }
  .body-copy h2 { font-size: 10.6px; font-weight: 700; }
  .body-copy p + p { margin-top: 6px; }

  .site-bar {
    height: 43px;
    flex: none;
    background: var(--charcoal);
    color: #fff;
    font-weight: 600;
    font-size: 13px;
    display: flex;
    align-items: center;
    justify-content: center;
  }

  .rates-area {
    height: 238px;
    flex: none;
    background: linear-gradient(90deg, #e6e6e6 0%, #fbfbfb 22%, #fbfbfb 78%, #e2e2e2 100%);
    padding: 12px 29px 0;
  }
  .rates {
    width: 100%;
    border-collapse: collapse;
    font-size: 12.4px;
    font-weight: 500;
    background: #fff;
  }
  .rates th, .rates td { border: 1px solid var(--rule); height: 26px; }
  .rates__title th {
    background: var(--red);
    color: #fff;
    font-weight: 700;
    font-family: "Barlow Semi Condensed", sans-serif;
    font-size: 14px;
    height: 28px;
    border-color: var(--red);
  }
  .rates__note td { text-align: center; }
  .rates__row td:first-child { text-align: left; padding-left: 8px; width: 51%; }
  .rates__row td:last-child { text-align: center; }
  .rates b { font-weight: 700; }
  .example {
    text-align: center;
    font-size: 12px;
    line-height: 1.3;
    margin-top: 10px;
  }

  .contact-bar {
    height: 85px;
    flex: none;
    background: var(--charcoal);
    color: #fff;
    display: flex;
    align-items: center;
    justify-content: space-between;
    padding: 0 28px 0 28px;
  }
  .contact-list { list-style: none; font-size: 9.6px; line-height: 1; }
  .contact-list li { display: flex; align-items: center; gap: 6px; margin: 4px 0; }
  .contact-list li:first-child { font-size: 10.5px; font-weight: 500; }
  .contact-list svg { width: 10px; height: 10px; flex: none; }
  .award { width: 66px; height: 66px; border-radius: 50%; background: var(--red); flex: none; }
</style>
</head>
<body>

<section class="card card--front">
  <header class="brand">
    <div class="brand__name"><span class="brand__mark"></span>THE KESTREL</div>
    <div class="brand__tagline">PRIVATE TRAINING STUDIO</div>
  </header>
  <div class="photo photo--coaches" role="img" aria-label="Photo of two trainers in the gym, one checking his watch and one holding battle ropes"></div>
  <h1 class="headline-band">A SAFE AND<br>INDIVIDUALIZED APPROACH<br>TO STRENGTH TRAINING.</h1>
  <div class="body-copy">
    <h2>OUR CLIENTS HAVE DIFFERENT GOALS:</h2>
    <p>Build strength, Increase Flexibility, Improve functional and daily movements, Train for an event, or Weight Loss. We will tailor your training program to the specific results you are looking for.</p>
    <p>Some ways of training increase the chance of injury, we do not practice those types of training at The Kestrel. Many of our clients have current or past injuries that can cause problems. We work with them to not aggravate those injuries or allow them to become an obstacle to their workouts.</p>
  </div>
  <footer class="site-bar">www.thekestrelfitness-example.com</footer>
</section>

<section class="card card--back">
  <header class="brand">
    <div class="brand__name"><span class="brand__mark"></span>THE KESTREL</div>
    <div class="brand__tagline">PRIVATE TRAINING STUDIO</div>
  </header>
  <div class="photo photo--suspension" role="img" aria-label="Photo of a trainer coaching a client using suspension straps against a wood-panelled wall"></div>
  <div class="rates-area">
    <table class="rates">
      <tr class="rates__title"><th colspan="2">OUR RATES:</th></tr>
      <tr class="rates__note"><td colspan="2">All Sessions are 60 minutes</td></tr>
      <tr class="rates__row"><td><b>1</b> time per week:</td><td>$<b>110</b> per session</td></tr>
      <tr class="rates__row"><td><b>2</b> times per week:</td><td>$<b>85</b> per session</td></tr>
      <tr class="rates__row"><td><b>3</b> times per week:</td><td>$<b>80</b> per session</td></tr>
      <tr class="rates__note"><td colspan="2">Add $<b>40</b> for a Partnered Session</td></tr>
    </table>
    <p class="example"><b>Example:</b> A Partnered Session<br>(2 people training together) coming twice<br>a week is $<b>125</b> per session</p>
  </div>
  <footer class="contact-bar">
    <ul class="contact-list">
      <li><svg viewBox="0 0 10 10"><circle cx="5" cy="5" r="4.4" fill="none" stroke="#e8323a" stroke-width="1"/><path d="M3.3 3c.2 1.8 1.6 3.4 3.5 3.8l.5-.8-.9-.5-.4.4c-.7-.3-1.3-.9-1.6-1.6l.4-.4-.5-.9z" fill="#e8323a"/></svg>(555) 014-2290</li>
      <li><svg viewBox="0 0 10 10"><circle cx="5" cy="5" r="4.4" fill="none" stroke="#e8323a" stroke-width="1"/><path d="M5 2.4a1.7 1.7 0 0 0-1.7 1.7C3.3 5.4 5 7.5 5 7.5s1.7-2.1 1.7-3.4A1.7 1.7 0 0 0 5 2.4z" fill="#e8323a"/></svg>42 Alder Lane, Riverton, NC</li>
      <li><svg viewBox="0 0 10 10"><circle cx="5" cy="5" r="4.4" fill="none" stroke="#e8323a" stroke-width="1"/><rect x="2.8" y="3.4" width="4.4" height="3.2" fill="#e8323a"/><path d="M2.8 3.4 5 5.2l2.2-1.8" fill="none" stroke="#2a2a2a" stroke-width=".6"/></svg>contact@thekestrelfitness-example.com</li>
      <li><svg viewBox="0 0 10 10"><circle cx="5" cy="5" r="4.4" fill="none" stroke="#e8323a" stroke-width="1"/><circle cx="5" cy="5" r="2.3" fill="none" stroke="#e8323a" stroke-width=".7"/><path d="M2.7 5h4.6M5 2.7c-1.2 1.4-1.2 3.2 0 4.6M5 2.7c1.2 1.4 1.2 3.2 0 4.6" fill="none" stroke="#e8323a" stroke-width=".6"/></svg>www.thekestrelfitness-example.com</li>
    </ul>
    <div class="award" role="img" aria-label="Award badge"></div>
  </footer>
</section>

</body>
</html>
```